Olive oil labels

We are a small company of traditional products Olive oil, honey, pollen and various liqueurs and we would like to create an appealing and elegant label for our olive oil.
Use the True Measure logo. Design #: 4358934
Can or can not use the Castle.
Can be one or two labels (front and back)
Have to have all the text.
- Azeite Virgem Extra - In great prominence
- Azeite de categoria superior obtido diretamente de azeitonas, unicamente por processo mecânico.
- Edição Limitada
- produzido e embalado por BLT
- consumir preferência antes do fim de
- Lote
- Vilarinho-Fontelas | Trás-os-Montes
- Portugal
- vardomar.lda@quintamail.example
(It has various sizes * 250ml (w4cmXh11cm)* 500ml (w9cmxh7) *750ml (w7xh13) *5L (w12cmxh14cm)

Target Market(s)

People with money expensive product but very good and in small quantity.

Industry/Entity Type

It Company

Font styles to use
Serif
Script

Colors

Designer to choose colors to be used in the design.

Requirements
Must have
• The tower of Fontelas - attached image
Nice to have
• Maybe have written extra virgin olive oil in Portuguese " Azeite Virgem Extra" and English .
• Black label preference.

```html
<!DOCTYPE html>
<html lang="pt">
<head>
<meta charset="utf-8">
<title>Vardomar — Azeite Virgem Extra</title>
<link rel="stylesheet" href="https://fonts.googleapis.com/css2?family=Playfair+Display:wght@500;700&family=Roboto+Condensed:wght@400&family=Arimo:wght@400;700&display=swap">
<style>
  :root {
    --paper: #ffffff;
    --label: #231f20;
    --gold: #b49a5e;
    --ink: #ffffff;
    --leaf: #3c3a3a;
    --leaf-fade: rgba(60, 58, 58, 0);
    --art: #2e2a2b;
  }
  * { margin: 0; padding: 0; box-sizing: border-box; }
  html, body { width: 880px; height: 1200px; overflow: hidden; background: var(--paper); }
  .canvas { position: relative; width: 880px; height: 1200px; }

  .label { position: absolute; background: var(--label); overflow: hidden; }
  .label--front { left: 44px; top: 32px; width: 380px; height: 1134px; }
  .label--back  { left: 457px; top: 316px; width: 378px; height: 566px; }

  .foliage { position: absolute; border-radius: 50%;
    background: radial-gradient(closest-side, var(--leaf), var(--leaf-fade)); }

  .serif-display {
    font-family: "Playfair Display", "Times New Roman", serif;
    color: var(--gold);
    position: absolute; left: -200px; right: -200px; text-align: center;
    transform: scaleX(0.72); transform-origin: center;
    line-height: 1; white-space: nowrap;
  }

  .brand-mark { position: absolute; left: 134px; top: 130px; width: 112px; height: 112px;
    border-radius: 50%; background: var(--gold); }
  .brand-name { top: 280px; font-size: 50px; font-weight: 500; letter-spacing: 1px; }

  .tower-art { position: absolute; left: 92px; top: 384px; width: 196px; height: 122px;
    background: linear-gradient(180deg, var(--label), var(--art)); }

  .product-name { font-weight: 700; font-size: 104px; letter-spacing: -2px; transform: scaleX(0.66); }
  .product-name--1 { top: 548px; }
  .product-name--2 { top: 656px; }
  .product-name--3 { top: 764px; }

  .english-name { position: absolute; left: 92px; top: 938px; width: 196px; height: 74px; }
  .english-name .rule { position: absolute; left: 0; right: 0; height: 2px; background: var(--ink); }
  .english-name .rule--t1 { top: 0; } .english-name .rule--t2 { top: 6px; }
  .english-name .rule--b1 { top: 66px; } .english-name .rule--b2 { top: 72px; }
  .english-name .text { position: absolute; left: -100px; right: -100px; top: 8px; text-align: center;
    font-family: "Playfair Display", "Times New Roman", serif; font-weight: 500; font-size: 60px;
    color: var(--ink); line-height: 1; transform: scaleX(0.72); white-space: nowrap; }

  .cond { font-family: "Roboto Condensed", "Arial Narrow", sans-serif; color: var(--ink); position: absolute; white-space: nowrap; }
  .statement { top: 27px; font-size: 18px; line-height: 27px; }
  .statement--left { left: 49px; }
  .statement--right { left: 217px; }
  .statement-divider { position: absolute; left: 197px; top: 26px; width: 2px; height: 104px; background: var(--ink); }

  .back-brand { top: 156px; font-size: 36px; font-weight: 500; letter-spacing: 1px; }

  .address { left: 46px; font-size: 20px; line-height: 1; }
  .sans { font-family: "Arimo", Arial, sans-serif; color: var(--ink); position: absolute; left: 46px; white-space: nowrap; line-height: 1; }
  .volume { top: 384px; font-size: 34px; }
  .edition { top: 446px; font-size: 16px; font-weight: 700; }
  .lot-caption { top: 474px; font-size: 12px; }
  .lot-box { position: absolute; top: 492px; height: 45px; background: var(--paper); }
  .lot-box--lot { left: 46px; width: 52px; }
  .lot-box--date { left: 109px; width: 88px; }
</style>
</head>
<body>
<div class="canvas">

  <section class="label label--front">
    <div class="foliage" role="img" aria-label="Olive branch decoration" style="left:-20px;top:-20px;width:160px;height:170px"></div>
    <div class="foliage" role="img" aria-label="Olive branch decoration" style="left:260px;top:-10px;width:140px;height:160px"></div>
    <div class="foliage" role="img" aria-label="Olive branch decoration" style="left:300px;top:300px;width:110px;height:200px"></div>
    <div class="foliage" role="img" aria-label="Olive branch decoration" style="left:-30px;top:720px;width:110px;height:200px"></div>
    <div class="foliage" role="img" aria-label="Olive branch decoration" style="left:-20px;top:980px;width:140px;height:170px"></div>
    <div class="foliage" role="img" aria-label="Olive branch decoration" style="left:250px;top:1000px;width:150px;height:150px"></div>

    <div class="brand-mark" aria-hidden="true"></div>
    <div class="serif-display brand-name">VARDOMAR</div>

    <div class="tower-art" role="img" aria-label="Line drawing of the tower of Fontelas"></div>

    <h1>
      <span class="serif-display product-name product-name--1">AZEITE</span>
      <span class="serif-display product-name product-name--2">VIRGEM</span>
      <span class="serif-display product-name product-name--3">EXTRA</span>
    </h1>

    <div class="english-name">
      <span class="rule rule--t1"></span><span class="rule rule--t2"></span>
      <span class="text">Olive Oil</span>
      <span class="rule rule--b1"></span><span class="rule rule--b2"></span>
    </div>
  </section>

  <section class="label label--back">
    <div class="foliage" role="img" aria-label="Olive branch decoration" style="left:280px;top:200px;width:120px;height:180px"></div>
    <div class="foliage" role="img" aria-label="Olive branch decoration" style="left:270px;top:400px;width:130px;height:190px"></div>

    <p class="cond statement statement--left">AZEITE<br>DE CATEGORIA<br>SUPERIOR OBTIDO<br>DIRETAMENTE</p>
    <span class="statement-divider"></span>
    <p class="cond statement statement--right">DE AZEITONAS,<br>UNICAMENTE<br>POR PROCESSO<br>MECÂNICO.</p>

    <div class="serif-display back-brand">VARDOMAR</div>

    <p class="cond address" style="top:206px">Vilarinho-Fontelas</p>
    <p class="cond address" style="top:231px">Trás-os-Montes</p>
    <p class="cond address" style="top:257px;font-size:24px">Portugal</p>
    <p class="cond address" style="top:286px">vardomar.lda@quintamail.example</p>
    <p class="cond address" style="top:317px">Produzido e embalado por:</p>
    <p class="cond address" style="top:342px">BLT</p>

    <p class="sans volume">500ml</p>
    <p class="cond address" style="top:420px;font-size:17px">AZEITE VIRGEM EXTRA</p>
    <p class="sans edition">Edição Limitada</p>
    <p class="sans lot-caption">Lote e Validade</p>
    <span class="lot-box lot-box--lot"></span>
    <span class="lot-box lot-box--date"></span>
  </section>

</div>
</body>
</html>
```